Korivan 43rd Festival

We need a poster design for the 43rd Korivan Youth Festival.
The festival will include a church service, folkloric dancing and a live band. The poster will be primarily in the Cyrillic language so it will need to be editable by us to confirm the writing.
I have attached a older design that we would like to use as a base. The new look of the poster is to be fresh and clean, i have attached an example of the new / clean poster. We would like to incorporate our countries nations colours, red, blue and white like in the example.

You will have to extract the text from the scanned 'old poster' pdf document

I have marked up a image 'my thoughts' to help

Once this poster is finalised we will engage with you further for to design menu poster, entry ticket design etc.

```html
<!DOCTYPE html>
<html lang="sr">
<head>
<meta charset="utf-8">
<title>Korivan Youth Festival</title>
<link href="https://fonts.googleapis.com/css2?family=Open+Sans:ital,wght@0,400;0,600;0,700;0,800;1,600;1,800&family=Raleway:wght@700&display=swap" rel="stylesheet">
<style>
  :root {
    --navy: #15457d;
    --flag-red: #d62f3a;
    --flag-red-deep: #c42632;
    --flag-blue: #2d4f9e;
    --orange: #f28a1e;
    --ink: #1d1d1f;
    --footer-red: #de1f2d;
    --ribbon-salmon: #f2b8a4;
    --ribbon-lilac: #b3b5d8;
    --title-red: #e0212e;
    --title-blue: #1f3f8e;
    --white: #ffffff;
  }
  * { margin: 0; padding: 0; box-sizing: border-box; }
  html, body { width: 815px; height: 1200px; overflow: hidden; background: var(--white); }
  body { font-family: "Open Sans", Arial, sans-serif; color: var(--ink); }
  .poster { position: relative; width: 815px; height: 1200px; overflow: hidden; background: var(--white); }

  .header {
    position: absolute; left: 0; top: 0; width: 100%; height: 132px;
    background: var(--navy); color: var(--white); text-align: center;
  }
  .header__org { position: absolute; top: 38px; width: 100%; font-size: 15px; font-weight: 400; }
  .header__name { position: absolute; top: 63px; width: 100%; font-size: 16.5px; font-weight: 700; }
  .header__blessing { position: absolute; top: 95px; width: 100%; font-size: 11px; }

  .hero-photo {
    position: absolute; left: 0; top: 132px; width: 100%; height: 650px;
    background:
      linear-gradient(180deg, rgba(255,255,255,0) 62%, #fff 100%),
      linear-gradient(100deg, rgba(255,255,255,0) 62%, rgba(255,255,255,0.75) 82%, #fff 96%),
      linear-gradient(155deg, var(--flag-red-deep) 0%, var(--flag-red) 42%, #b8384c 50%, var(--flag-blue) 58%, #3d5fae 72%, #c9d2ea 88%, #fff 100%);
  }

  .festival-title {
    position: absolute; left: 0; top: 186px; width: 100%; text-align: center;
    color: var(--white); font-weight: 800; font-style: italic;
    font-size: 33px; line-height: 42px; letter-spacing: -0.3px;
    text-shadow: 0 2px 4px rgba(0,0,0,0.3);
  }
  .festival-title__rule {
    position: absolute; left: 340px; top: 278px; width: 136px; height: 4px; background: var(--white);
  }
  .festival-title__english {
    position: absolute; left: 0; top: 290px; width: 100%; text-align: center;
    font-family: "Raleway", Arial, sans-serif; font-weight: 700; font-size: 29px;
    color: var(--orange);
    text-shadow: 0 1px 2px rgba(60,0,0,0.7), 0 2px 6px rgba(0,0,0,0.45);
  }
  .venue {
    position: absolute; left: 130px; top: 360px; width: 500px; text-align: center;
    color: var(--white); font-weight: 700; font-size: 20px; line-height: 24px;
    white-space: nowrap;
    text-shadow: 0 1px 3px rgba(0,0,0,0.45);
  }

  .photo {
    position: absolute; border-radius: 50%; border: 3px solid var(--white);
    box-shadow: 0 2px 6px rgba(0,0,0,0.2);
  }
  .photo--monastery { left: 625px; top: 279px; width: 232px; height: 232px;
    background: linear-gradient(180deg, #d9e4ee 0%, #e7ecef 40%, #c08a62 55%, #a8734f 72%, #6f8a3e 85%, #5d7a32 100%); }
  .photo--folklore { left: 72px; top: 478px; width: 156px; height: 156px;
    background: linear-gradient(180deg, #d8e2e6 0%, #b7c7cf 35%, #8a3d3c 60%, #2b2b2b 85%, #c7b8a6 100%); }
  .photo--band { left: 179px; top: 540px; width: 200px; height: 200px;
    background: linear-gradient(180deg, #2a2a2c 0%, #4a4a4e 35%, #e8e6e2 60%, #e06a4a 80%, #3a3a3a 100%); }
  .photo--food { left: 85px; top: 693px; width: 216px; height: 216px;
    background: radial-gradient(circle at 50% 45%, #8a4a2a 0%, #6e3a20 40%, #c64a2a 70%, #f0e8e0 100%); }

  .schedule { position: absolute; left: 428px; top: 565px; width: 380px; }
  .schedule__day { font-weight: 700; font-size: 19px; line-height: 26px; color: var(--ink); }
  .schedule__list { list-style: none; margin: 4px 0 12px 20px; font-size: 14px; line-height: 20px; }
  .schedule__list li { display: flex; }
  .schedule__time { width: 48px; flex: none; }
  .schedule__first { margin: 4px 0 12px 22px; }

  .invite {
    position: absolute; left: 80px; top: 938px; width: 310px; text-align: center;
    font-weight: 800; font-size: 16px; line-height: 23px;
  }
  .invite__food { color: var(--title-red); }
  .invite__music { color: var(--title-blue); }

  .ribbon { position: absolute; left: 0; top: 990px; width: 815px; height: 140px; }

  .welcome {
    position: absolute; right: 58px; top: 1025px; width: 560px; text-align: right;
    font-weight: 700; font-size: 11.5px; line-height: 17px; color: var(--ink);
  }

  .footer {
    position: absolute; left: 0; top: 1126px; width: 100%; height: 74px;
    background: var(--footer-red); color: var(--white); text-align: center;
    font-style: italic; font-weight: 600; font-size: 14px; line-height: 74px;
  }
</style>
</head>
<body>
<main class="poster">
  <header class="header">
    <p class="header__org">Организациони одбор</p>
    <p class="header__name">Кориванске Заједнице Аустралијско-Новозеландске</p>
    <p class="header__blessing">са благословом нашег Преосвећеног Владике Господина Теодора организује и позива на</p>
  </header>

  <div class="hero-photo" role="img" aria-label="Waving red, blue and white national flag with coat of arms"></div>

  <h1 class="festival-title">ЧЕТРДЕСЕТ ТРЕЋИ КОРИВАНСКИ<br>ОМЛАДИНСКИ ФЕСТИВАЛ</h1>
  <div class="festival-title__rule"></div>
  <p class="festival-title__english">43rd Korivan Youth Festival</p>

  <p class="venue">Манастир Нова Равница<br>128 Birchfield Road - ELMWOOD - ACT 2690</p>

  <div class="photo photo--monastery" role="img" aria-label="Striped brick monastery church on a green lawn"></div>
  <div class="photo photo--folklore" role="img" aria-label="Folklore dance group in traditional costume"></div>
  <div class="photo photo--band" role="img" aria-label="Live band musicians"></div>
  <div class="photo photo--food" role="img" aria-label="Plate of grilled cevapi with ajvar and greens"></div>

  <section class="schedule">
    <h2 class="schedule__day">ПЕТАК 26 ЈАНУАР 2024</h2>
    <ul class="schedule__list schedule__first">
      <li><span class="schedule__time">18.00:</span><span>Часова Вечерње Богослужење</span></li>
    </ul>
    <h2 class="schedule__day">СУБОТА 27 ЈАНУАР 2024</h2>
    <ul class="schedule__list">
      <li><span class="schedule__time">10.00:</span><span>Света Архијерејска Литургија</span></li>
      <li><span class="schedule__time">12.30:</span><span>Отварање Фестивала</span></li>
      <li><span class="schedule__time">13.00:</span><span>Наступи фолклорних група и<br>народно весеље</span></li>
      <li><span class="schedule__time">18.00:</span><span>Вечерње Богослужење</span></li>
    </ul>
    <h2 class="schedule__day">НЕДЕЉА 28 ЈАНУАР 2024</h2>
    <ul class="schedule__list">
      <li><span class="schedule__time">00.00:</span><span>Света Литургија</span></li>
      <li><span class="schedule__time">11.30:</span><span>Наставак фолклорних група</span></li>
      <li><span class="schedule__time">16.00:</span><span>Недела пехара<br>Завршетак Фестивала</span></li>
    </ul>
  </section>

  <p class="invite">
    <span class="invite__food">ЧЕКА ВАС ДОМАЋИНСКА КУХИЊА</span><br>
    <span class="invite__music">И ПРИЈАТНА СРПСКА МУЗИКА</span>
  </p>

  <svg class="ribbon" viewBox="0 0 815 140" aria-hidden="true">
    <path d="M0 10 C120 0 200 18 260 40 C420 100 600 70 815 60 L815 90 C600 100 420 130 260 70 C200 48 120 32 0 40 Z" fill="var(--ribbon-salmon)"/>
    <path d="M0 40 C120 32 200 48 260 70 C420 130 600 100 815 90 L815 120 C600 130 420 150 260 100 C200 80 120 66 0 72 Z" fill="var(--ribbon-lilac)"/>
    <path d="M0 72 C120 66 200 80 260 100 C230 110 200 120 190 136 C170 110 100 100 0 104 Z" fill="#f4f4f8"/>
  </svg>

  <p class="welcome">ДОБРО НАМ ДОШЛИ У КОРИВАНСКУ СВЕТИЊУ СВИХ ВЕРНИХ СРБА<br>АУСТРАЛИЈЕ И НОВОГ ЗЕЛАНДА. И НА ПОКЛОЊЕЊЕ НЕДАВНО ПРИСТИГЛОЈ ИЗ<br>МАНАСТИРА СВЕТОГОРСКОГ СВЕТОЈ ИКОНИ БОГОРОДИЦИ ТРОЈЕРУЧИЦИ!</p>

  <footer class="footer">ЗА СВЕ ИНФОРМАЦИЈЕ ЈАВИТЕ СЕ НА ТЕЛ: 0400 718 245</footer>
</main>
</body>
</html>
```